Website for legal services (estates law) called KTV ESTATES LAW

Simple, catchy and easy to use. I am providing estates legal services and I want clients to feel a warm, friendly but professional vibe when they visit my website. I don't want harsh legal pictures (like a picture of a tough lawyer, or pictures of scales of justice). Pictures of books, plants, signing documents or a comfortable looking office are acceptable.

Please use wordpress to design it because I want ability to upload blogs on my own through wordpress after. I am attaching my logo.

Target Market(s)

Millenials, boomers, people in their 40's and anyone looking to transfer property titles or create a will, or anyone whose relatives have died and need help with estates administration.

Industry/Entity Type

Law Firm

Coding

Coded - Design and coding required

Number of Pages Required

4 page

Font styles to use
Sans Serif

Colors
0493ce
33a6d7
85cae6
cee9f5
f4fafd

Requirements
Must have
• - Must be designed with WordPress
- Must have a warm, friendly, professional vibe
- I want to be able to edit any of the content of the website myself
Nice to have
• Pictures of law books, plants, signing documents or a comfortable looking office are acceptable.
Should not have
• I don't want harsh legal pictures (like a picture of a tough lawyer, or pictures of scales of justice).

```html
<!DOCTYPE html>
<html lang="en">
<head>
<meta charset="utf-8">
<title>KTV Estates Law</title>
<link href="https://fonts.googleapis.com/css2?family=Roboto:wght@300;400;500;700&display=swap" rel="stylesheet">
<style>
:root{
  --blue:#0493ce;
  --blue-mid:#33a6d7;
  --blue-soft:#85cae6;
  --blue-pale:#cee9f5;
  --blue-mist:#f4fafd;
  --ink:#111;
  --text:#2b2b2b;
  --white:#fff;
}
*{box-sizing:border-box;margin:0;padding:0}
html,body{width:1200px;height:3854px;overflow:hidden}
body{position:relative;background:var(--white);font-family:'Roboto',sans-serif;color:var(--text)}
.photo{position:absolute}

/* hero */
.hero{position:absolute;left:0;top:0;width:1200px;height:690px;background:var(--blue-mist)}
.hero-photo{position:absolute;left:0;top:0;width:1200px;height:690px}
.brand{position:absolute;left:120px;top:112px;display:flex;align-items:center;gap:10px;font-size:22px;font-weight:500;color:var(--ink);letter-spacing:1px}
.brand-mark{width:16px;height:16px;background:var(--blue)}
.nav{position:absolute;top:46px;left:612px}
.nav a{position:absolute;font-size:18px;font-weight:700;color:var(--ink);text-decoration:none;white-space:nowrap}
.hero-copy{position:absolute;left:112px;top:308px;width:440px;font-size:18px;line-height:28.5px;color:var(--ink)}
.hero-copy p+p{margin-top:28px}

/* headings */
.heading{position:absolute;font-size:33px;font-weight:400;color:var(--ink);letter-spacing:.5px}
.rule{position:absolute;height:1px;background:var(--blue-mid)}

/* about */
.about-copy{position:absolute;left:123px;top:870px;width:520px;font-size:16px;line-height:28.3px;color:var(--ink)}
.about-copy p+p{margin-top:28px}
.quote-box{position:absolute;left:118px;top:1137px;width:536px;height:90px;background:var(--blue-pale);padding:16px 30px;font-size:16px;line-height:28px;color:var(--ink)}

/* services */
.services-intro{position:absolute;left:122px;top:1430px;font-size:16px;height:20px;overflow:hidden;color:var(--ink)}
.estate-panel{position:absolute;left:434px;top:1499px;width:766px;height:678px;background:var(--blue-mist)}
.service-title{position:absolute;font-size:45px;font-weight:500;color:var(--blue)}
.service-copy{position:absolute;font-size:16px;line-height:24px;color:var(--ink)}
.service-copy ul{list-style:none}
.service-copy li{padding-left:30px;position:relative}
.service-copy li::before{content:"•";position:absolute;left:0;font-size:12px}
.service-copy .gap{height:22px}
.realestate-panel{position:absolute;left:0;top:2177px;width:768px;height:594px;background:var(--blue-pale)}

/* blog */
.card{position:absolute;top:2967px;width:239px}
.card-img{width:239px;height:186px}
.card h3{font-size:22px;font-weight:400;color:var(--ink);margin-top:22px;line-height:38px}
.card p{font-size:14.5px;line-height:24px;color:var(--ink);margin-top:6px;white-space:nowrap}

/* contact */
.form-card{position:absolute;left:109px;top:3495px;width:392px;height:359px;background:var(--white);box-shadow:0 0 6px rgba(4,147,206,.35)}
.field{position:absolute;left:27px;width:338px;height:30px;border:1px solid var(--blue-soft);font-size:10px;color:#9ab;padding:7px 12px}
.send{position:absolute;left:27px;top:256px;width:338px;height:32px;background:var(--blue);color:var(--white);font-size:15px;text-align:center;line-height:32px;letter-spacing:.5px}
.hours{position:absolute;left:553px;top:3508px;color:var(--ink)}
.hours h4{font-size:22px;font-weight:400;margin-bottom:10px}
.hours p{font-size:16px;line-height:24px}
.contact-band{position:absolute;left:501px;top:3636px;width:699px;height:194px;background:var(--blue-pale)}
.contact-col{position:absolute;top:3740px;font-size:15px;line-height:22px;color:var(--ink)}
.icon{position:absolute;top:3690px;width:40px;height:40px}
.footer{position:absolute;left:0;top:3830px;width:1200px;height:24px;background:var(--blue);color:var(--white);font-size:11px;padding:6px 108px}
</style>
</head>
<body>

<header class="hero">
  <svg class="hero-photo" viewBox="0 0 1200 690" role="img" aria-label="City square with a tall glass office tower and people walking">
    <defs>
      <linearGradient id="city" x1="0" y1="0" x2="0" y2="1">
        <stop offset="0" stop-color="#cee9f5"/>
        <stop offset=".55" stop-color="#85cae6"/>
        <stop offset="1" stop-color="#e4f3fa"/>
      </linearGradient>
    </defs>
    <polygon points="576,0 1200,0 1200,690 471,690" fill="url(#city)"/>
  </svg>
  <div class="brand"><span class="brand-mark"></span>KTV ESTATES LAW</div>
  <nav class="nav">
    <a style="left:0">HOME</a>
    <a style="left:93px">ABOUT</a>
    <a style="left:193px">SERVICES</a>
    <a style="left:317px">BLOG</a>
    <a style="left:405px">CONTACT</a>
  </nav>
  <div class="hero-copy">
    <p>Thank you for visiting KTV Estates Law,<br>where I endeavor to earn your trust and provide<br>you with high quality estates and real estate<br>law services.</p>
    <p>My goal is to make you feel comfortable<br>as soon as you step foot in my office.</p>
  </div>
</header>

<section class="about">
  <h2 class="heading" style="left:123px;top:795px">ABOUT</h2>
  <div class="rule" style="left:280px;top:818px;width:320px"></div>
  <div class="about-copy">
    <p>My name is Marina Delacourt and I am an estates and real estate<br>lawyer. I graduated from Northbridge University Faculty of Law<br>and my passion is estates law and real estate law.</p>
    <p>Prior to entering the legal profession, I obtained my CPA<br>(Chartered Professional Accounting) designation and worked<br>in business and management accounting for many years,<br>where I developed a deeper understanding of money and<br>finances.</p>
  </div>
  <div class="quote-box">As a lawyer, I lean on this foundation frequently for the<br>benefit of my clients.</div>
  <div class="photo" style="left:718px;top:799px;width:252px;height:205px;background:var(--blue-mid)"></div>
  <div class="photo" role="img" aria-label="Portrait of the lawyer in a dark suit" style="left:654px;top:827px;width:251px;height:415px;background:linear-gradient(180deg,#cee9f5,#1d5f80)"></div>
  <div class="photo" role="img" aria-label="Pen resting on financial charts" style="left:905px;top:1002px;width:195px;height:210px;background:linear-gradient(135deg,#f4fafd,#b9dcec)"></div>
</section>

<section class="services">
  <h2 class="heading" style="left:123px;top:1368px">SERVICES</h2>
  <div class="rule" style="left:325px;top:1390px;width:775px"></div>
  <p class="services-intro">I use my accounting background to provide a high quality legal experience for my estates and real estate clients.</p>

  <div class="photo" role="img" aria-label="Fountain pen lying on a last will and testament" style="left:0;top:1499px;width:434px;height:678px;background:linear-gradient(160deg,#1f6f92,#85cae6 55%,#eaf6fb)"></div>
  <div class="estate-panel"></div>
  <h3 class="service-title" style="left:474px;top:1537px">Estate Law</h3>
  <div class="service-copy" style="left:478px;top:1629px;width:640px">
    <p>I offer the following services as part of an estate plan:</p>
    <div class="gap"></div>
    <ul>
      <li>Wills (personal, corporate, foreign property);</li>
      <li>Trusts;</li>
      <li>Powers of Attorney for Personal Care and Property;</li>
      <li>Asset planning to minimize income tax and estate administration tax</li>
    </ul>
    <p>upon your passing.</p>
    <div class="gap" style="height:34px"></div>
    <p>I help administer &nbsp;entire estates &nbsp;including:</p>
    <div class="gap" style="height:14px"></div>
    <ul>
      <li>Guide the executor with the administration of an entire estate;</li>
      <li>Apply for the Certificate of Appointment of Estate Trustee with/without a Will</li>
    </ul>
    <p>(Applying for Probate);</p>
    <ul>
      <li>Administer trusts;</li>
      <li>Provide guidance about the requirements of financial institutions,</li>
    </ul>
    <p>the government, the courts;</p>
    <ul>
      <li>Draft documents required in dealing with various institutions;</li>
      <li>Applying for the Canada Pension Plan Death Benefit;</li>
      <li>Applying for the Estate Information Return.</li>
    </ul>
  </div>

  <div class="realestate-panel"></div>
  <div class="photo" role="img" aria-label="Stack of white binders and books" style="left:768px;top:2177px;width:432px;height:594px;background:linear-gradient(110deg,#e6f4fa,#ffffff 45%,#bfe0ee)"></div>
  <h3 class="service-title" style="left:123px;top:2315px">Real Estate Law</h3>
  <div class="service-copy" style="left:123px;top:2404px;width:600px">
    <p>I help clients with their residential sales, purchases and property transfer<br>needs. My clients’ real estate and estate needs often intersect, and for this<br>reason, I offer the following specialized services:</p>
    <div class="gap" style="height:36px"></div>
    <ul>
      <li>Transfers of title to family members or spouses;</li>
      <li>Transfers of title from deceased to survivors;</li>
      <li>Transfers of title to estate trustee for the purposes of selling the estate’s</li>
    </ul>
    <p>real estate asset.</p>
  </div>
</section>

<section class="blog">
  <h2 class="heading" style="left:108px;top:2878px">BLOG &amp; RESOURCES</h2>
  <div class="rule" style="left:479px;top:2900px;width:631px"></div>
  <article class="card" style="left:108px">
    <div class="card-img" role="img" aria-label="Hand signing a document with a pen" style="background:linear-gradient(135deg,#f4fafd,#b9dcec)"></div>
    <h3>Making a Will</h3>
    <p>Donec rutrum congue leo eget<br>malesuada. Mauris blandit ali-<br>quet elit, eget tincidunt nibh<br>pulvinar a. Curabitur arcu erat,<br>accumsan id imperdiet et, portti-</p>
  </article>
  <article class="card" style="left:362px">
    <div class="card-img" role="img" aria-label="Open book in front of library shelves" style="background:linear-gradient(180deg,#5a4638,#b8a591)"></div>
    <h3>Interesting facts</h3>
    <p>Donec rutrum congue leo eget<br>malesuada. Mauris blandit ali-<br>quet elit, eget tincidunt nibh<br>pulvinar a. Curabitur arcu erat,<br>accumsan id imperdiet et, portti-</p>
  </article>
  <article class="card" style="left:618px">
    <div class="card-img" role="img" aria-label="Stack of paper files on a desk" style="background:linear-gradient(180deg,#f4f4f4,#b49a7c)"></div>
    <h3 style="margin-top:18px">Interesting facts</h3>
    <p>Donec rutrum congue leo eget<br>malesuada. Mauris blandit ali-<br>quet elit, eget tincidunt nibh<br>pulvinar a. Curabitur arcu erat,<br>accumsan id imperdiet et, portti-</p>
  </article>
  <article class="card" style="left:872px">
    <div class="card-img" role="img" aria-label="Row of white books on a shelf" style="background:linear-gradient(90deg,#e6f4fa,#ffffff,#cee9f5)"></div>
    <h3 style="margin-top:18px">You must read<br>this books</h3>
    <p style="margin-top:18px">Donec rutrum congue leo eget<br>malesuada. Mauris blandit ali-<br>quet elit, eget tincidunt nibh</p>
  </article>
</section>

<section class="contact">
  <h2 class="heading" style="left:108px;top:3415px">STAY IN TOUCH</h2>
  <div class="rule" style="left:400px;top:3434px;width:710px"></div>

  <div class="contact-band"></div>
  <form class="form-card">
    <div class="field" style="top:39px">Name</div>
    <div class="field" style="top:80px">Your Email</div>
    <div class="field" style="top:120px">Phone Number</div>
    <div class="field" style="top:162px;height:82px">Message</div>
    <div class="send">SEND</div>
  </form>

  <div class="hours">
    <h4>Opening Hours</h4>
    <p>Monday – Friday: &nbsp;&nbsp;&nbsp;8.30 – 18.30</p>
    <p>Saturday: &nbsp;&nbsp;&nbsp;10.30 – 16.30</p>
    <p>Sunday:10.30 – 16.30</p>
  </div>

  <svg class="icon" style="left:570px" viewBox="0 0 40 40" fill="none" stroke="#0493ce" stroke-width="1.5" aria-hidden="true">
    <rect x="4" y="6" width="8" height="28" rx="2"/><rect x="12" y="10" width="24" height="24" rx="2"/>
    <rect x="17" y="14" width="14" height="5"/><path d="M18 23h2M23 23h2M28 23h2M18 28h2M23 28h2M28 28h2"/>
  </svg>
  <svg class="icon" style="left:764px" viewBox="0 0 40 40" fill="none" stroke="#0493ce" stroke-width="1.5" aria-hidden="true">
    <rect x="5" y="17" width="16" height="9" rx="4.5" transform="rotate(-45 13 21.5)"/>
    <rect x="19" y="13" width="16" height="9" rx="4.5" transform="rotate(-45 27 17.5)"/>
  </svg>
  <svg class="icon" style="left:952px" viewBox="0 0 40 40" fill="none" stroke="#0493ce" stroke-width="1.5" aria-hidden="true">
    <path d="M20 26c-5-6-8-10-8-14a8 8 0 0 1 16 0c0 4-3 8-8 14z"/><circle cx="20" cy="12" r="3"/>
    <path d="M10 24l-6 12h32l-6-12M14 36l4-8M26 36l-4-8"/>
  </svg>

  <div class="contact-col" style="left:540px">T: 555.014.2210<br>F: 555.014.2299</div>
  <div class="contact-col" style="left:718px">marina@ktv-law.ca<br>www.ktv-law.ca</div>
  <div class="contact-col" style="left:913px">2100 Harbour Avenue,<br>Suite 1901, Toronto ON<br>M4B2K7</div>
</section>

<footer class="footer">Copyright © KTV Estate Law</footer>

</body>
</html>
```